Tavner Golf Academy Brochure Design Project

We need a tri- fold brochure for our golf academy. Tavner Golf Academy was founded by Dale Tavner, a strength coach on the NLK Circuit. Our Academy fuses Swing instruction, 3D biomechanic analysis and fitness training. We would like to incorporate the colors green, grey/silver and possible black. The final design should communicate movement/action and health.
Updates
The brochure is tri fold, double sided. Front cover should include logo, and a photo of a golfer. inside should include a a history of our company, and the services we offer(I will provide). Back middle panel should be white, with logo on the top and space for address and contact info on the bottom (we currently have 2 locations, and may want to tailor this information). The other fold in should include testamonials (I will provide). Thank you.
Include the following Titles, pictures and descriptions under 'Service'
Industry/Entity Type
Fitness
Requirements
Must have
- photos of people recieving golf instruction, people performing functional exercise training (stability balls, tubing, medicine balls, stretching) We would like to designate a space to give a description of each of our services: 1)Golf Performance Evaluation. 2)Swing Coaching. 3)3D and Video Feedback Coaching. 4)Golf Performance (fitness) Coaching.
Testimonials from the Pros:
“I have trained exclusively with Dale for the last several years. Under his guidance, I have greatly enhanced my power, flexibility, and endurance on the course. As Head Strength and Conditioning Coach for the NLK, Dale personalizes cutting-edge golf fitness programs for me, so I know that every day I play, I am at the top of my game. As Dale’s fitness student and friend, I will thoroughly enjoy watching him create one of the world’s foremost golf performance companies.” - Tod Bramwell, 16 time NLK Circuit winner, Winner of the 2003 Corvane Classic, 2010 Halvery Trophy Champion
“Dale has really helped me take my golf fitness to the next level. Preventing injury, strength training, stability, flexibility, and generating power are some of the areas we have worked on and improved!” - Matías Orduna, 3 time NLK Circuit winner, 3 time Westmarch State College All American, 2 time KLQ Player of the Year
“Dale Tavner is one of the most knowledgeable and enthusiastic trainers in the business. Whether it be golf specific, bust your butt or light stretching, Dale has a varied, experienced and fun way to train!”- Glen Purdey, Winner, 2005 Morton Quill Award, 8 time NLK Circuit winner, 20 professional wins
“I trust and rely on Dale to get me ready for every round of golf that I play on the NLK Circuit. He is definitely one of the best in the industry.”- Wendell Pruitt, NLK Circuit Professional Golfer, Winner, 2007 Lyle Dunmore Vantrex Invitational, 2010 Ostrava Mutual Championship
“Since I started working with Dale my endurance, flexibility and strength have improved dramatically. His golf specific program has really shored up the weak areas of my body. He has also really helped me come back from my knee and back injuries.” - Lonnie Gressett, 4 time NLK Circuit Winner

```html
<!DOCTYPE html>
<html lang="en">
<head>
<meta charset="utf-8">
<title>Tavner Golf Academy – Services &amp; Testimonials</title>
<link rel="stylesheet" href="https://fonts.googleapis.com/css2?family=Satisfy&family=Source+Sans+3:wght@400;600&display=block">
<style>
  :root{
    --green:#3f6d3a;
    --green-dark:#375f33;
    --green-head:#3d6a33;
    --yellow:#f3e21a;
    --quote-name:#f2e64a;
    --body-grey:#6a6a6a;
    --white:#ffffff;
  }
  *{box-sizing:border-box;margin:0;padding:0}
  html,body{width:1200px;height:927px;overflow:hidden;background:#fff}
  .brochure{position:relative;width:1200px;height:927px;font-family:"Source Sans 3",Arial,sans-serif}

  .ln{display:block;white-space:nowrap;text-align:justify;text-align-last:justify}
  .ln.end{text-align-last:left}

  /* Services panel */
  .panel-services{position:absolute;left:0;top:0;width:400px;height:927px;
    background:linear-gradient(90deg,#ffffff 0%,#f1f2f3 55%,#d9dbdd 100%)}
  .services-title{position:absolute;left:22px;top:15px;font-size:22px;font-weight:400;color:var(--green-head)}
  .service-name{position:absolute;font-size:19px;font-weight:400;color:var(--green-head);white-space:nowrap;line-height:24px}
  .service-photo{position:absolute;left:0;width:180px;border-top:5px solid var(--yellow);border-bottom:5px solid var(--yellow)}
  .service-text{position:absolute;left:193px;width:188px;font-size:15px;line-height:27.2px;color:var(--body-grey)}
  .service-text.ragged .ln{text-align-last:left}

  /* Testimonial panels */
  .panel-middle{position:absolute;left:400px;top:0;width:400px;height:927px;background:var(--green)}
  .panel-right{position:absolute;left:800px;top:0;width:400px;height:927px;background:var(--green);border-left:1px solid var(--green-dark)}
  .hero-photo{position:absolute;left:0;top:0;width:400px;height:336px;
    background:linear-gradient(180deg,#5d8fd6 0%,#a9c9ec 32%,#4e7d2c 45%,#7fae3a 75%,#5f8f25 100%);
    border-bottom:3px solid var(--yellow)}

  .quote{position:absolute;font-family:"Satisfy",cursive;font-size:14.5px;line-height:27.2px;color:var(--white)}
  .by{font-family:"Source Sans 3",Arial,sans-serif;font-size:13.5px;color:var(--quote-name)}
  .polaroid{position:absolute;background:#fff;padding:4px;box-shadow:2px 3px 6px rgba(0,0,0,.45)}
  .polaroid .shot{width:100%;height:100%;display:flex;align-items:flex-end;justify-content:center}
  .polaroid .tag{font-family:"Source Sans 3",Arial,sans-serif;font-weight:600;font-size:11px;letter-spacing:.5px;color:#fff;padding:0 6px 6px}
  .polaroid .tag.top{align-self:flex-start;padding:6px 6px 0}
</style>
</head>
<body>
<div class="brochure">

  <section class="panel-services">
    <h2 class="services-title">Our Services</h2>

    <h3 class="service-name" style="left:22px;top:60px">Swing Coaching:</h3>
    <div class="service-photo" role="img" aria-label="Golfer finishing a swing on a course under blue sky"
         style="top:90px;height:258px;background:linear-gradient(180deg,#7fa9e0 0%,#c9dcf1 45%,#7f9b5a 75%,#4f7a2a 100%)"></div>
    <p class="service-text" style="top:61px">
      <span class="ln">Swing Coaching focuses on</span>
      <span class="ln">teaching the fundamentals</span>
      <span class="ln">of the golf swing from the</span>
      <span class="ln">set-up, grip, aim, alignment,</span>
      <span class="ln end">and club path.</span>
    </p>

    <h3 class="service-name" style="left:22px;top:375px">3D Biomechanics:</h3>
    <div class="service-photo" role="img" aria-label="Golfer in a motion capture studio with a 3D swing analysis screen"
         style="top:402px;height:156px;background:linear-gradient(90deg,#1a1f1a 0%,#2b3a2a 45%,#e9ece6 60%,#cfd6cc 100%)"></div>
    <p class="service-text" style="top:374px">
      <span class="ln">Our 3D Biomechanics train-</span>
      <span class="ln">ing focuses on developing an</span>
      <span class="ln">efficient golf swing via the</span>
      <span class="ln">kinematic sequence. Effort-</span>
      <span class="ln">less power and a safe, effi-</span>
      <span class="ln">cient and reproducible</span>
      <span class="ln end">swing are developed.</span>
    </p>

    <h3 class="service-name" style="left:6px;top:612px">Performance training:</h3>
    <div class="service-photo" role="img" aria-label="Trainer coaching a client seated on a stability ball in a gym"
         style="top:642px;height:247px;background:linear-gradient(180deg,#e8e6e0 0%,#d4cbbd 55%,#b98b52 80%,#a8763f 100%)"></div>
    <p class="service-text ragged" style="top:612px">
      <span class="ln">Performance Training fo-</span>
      <span class="ln">cuses on improving specific</span>
      <span class="ln">mobility, stability and core</span>
      <span class="ln">strength that allow golfer's</span>
      <span class="ln">to feel and play their best.</span>
      <span class="ln">Other exercises strategies</span>
      <span class="ln">are also employed to pro-</span>
      <span class="ln">duce efficient, powerful and</span>
      <span class="ln">durable golfers</span>
    </p>
  </section>

  <section class="panel-middle">
    <div class="hero-photo" role="img" aria-label="Golf ball on a green fairway with a flag and palm trees behind"></div>

    <div class="polaroid" style="left:237px;top:350px;width:134px;height:140px;transform:rotate(-2deg)">
      <div class="shot" role="img" aria-label="Portrait of Lonnie Gressett swinging a club" style="background:linear-gradient(180deg,#6f8c6a,#3e4a3a)"><span class="tag">LONNIE GRESSETT</span></div>
    </div>
    <blockquote class="quote" style="left:26px;top:359px;width:346px">
      <span class="ln" style="width:192px">“Since I started working with</span>
      <span class="ln" style="width:192px">Dale my endurance, flexibility</span>
      <span class="ln" style="width:192px">and strength have improved</span>
      <span class="ln" style="width:192px">dramatically. His golf specific</span>
      <span class="ln" style="width:192px">program has really shored up the</span>
      <span class="ln">weak areas of my body. He has also really helped me come</span>
      <span class="ln">back from my knee and back injuries.” <span class="by">-- Lonnie Gressett, 4</span></span>
      <span class="ln end by">time NLK Circuit Winner</span>
    </blockquote>

    <div class="polaroid" style="left:112px;top:605px;width:173px;height:128px;transform:rotate(3deg)">
      <div class="shot" role="img" aria-label="Matías Orduna crouched low reading a putt" style="background:linear-gradient(180deg,#8fae6e,#5a7a3e)"><span class="tag top">MATÍAS ORDUNA</span></div>
    </div>

    <blockquote class="quote" style="left:26px;top:743px;width:346px">
      <span class="ln">“Dale has really helped me take my golf fitness to the next</span>
      <span class="ln">level. Preventing injury, strength training, stability, flexibility,</span>
      <span class="ln">and generating power are some of the areas we have worked on</span>
      <span class="ln">and improved!” <span class="by">-- Matías Orduna, 3 time NLK Circuit winner,</span></span>
      <span class="ln by">3 time Westmarch State College All American,</span>
      <span class="ln end by">2 time KLQ Player of the Year</span>
    </blockquote>
  </section>

  <section class="panel-right">
    <div class="polaroid" style="left:26px;top:30px;width:136px;height:160px;transform:rotate(-2deg)">
      <div class="shot" role="img" aria-label="Glen Purdey crouching on the green" style="background:linear-gradient(180deg,#a7c0d8,#5f8a4a)"></div>
    </div>
    <blockquote class="quote" style="left:180px;top:28px;width:193px">
      <span class="ln">“Dale Tavner is one of the most</span>
      <span class="ln">knowledgeable and enthusiastic</span>
      <span class="ln">trainers in the business. Whether</span>
      <span class="ln">it be golf specific, bust your butt or</span>
      <span class="ln">light streching, Dale has a varied,</span>
      <span class="ln">experienced and fun way to train!”</span>
    </blockquote>
    <p class="quote" style="left:26px;top:192px;width:350px">
      <span class="ln end by">-- Glen Purdey, Winner, 2005 Morton Quill Award, 8 time</span>
      <span class="ln end by">NLK Circuit winner, 20 professional wins</span>
    </p>

    <div class="polaroid" style="left:222px;top:270px;width:142px;height:166px;transform:rotate(-3deg)">
      <div class="shot" role="img" aria-label="Tod Bramwell following through on a swing" style="background:linear-gradient(180deg,#4e5a4e,#2c332c)"><span class="tag">TOD BRAMWELL</span></div>
    </div>
    <blockquote class="quote" style="left:24px;top:279px;width:350px">
      <span class="ln" style="width:191px">“I have trained exclusively with</span>
      <span class="ln" style="width:191px">Dale for the last several years.</span>
      <span class="ln" style="width:191px">Under his guidance, I have</span>
      <span class="ln" style="width:191px">greatly enhanced my power, flex-</span>
      <span class="ln" style="width:191px">ibility, and endurance on the</span>
      <span class="ln" style="width:191px">course. As Head Strength and</span>
      <span class="ln">Conditioning Coach for the NLK, Dale personalizes cutting-</span>
      <span class="ln">edge golf fitness programs for me, so I know that every day I</span>
      <span class="ln">play, I am at the top of my game. As Dale’s fitness student</span>
      <span class="ln">and friend, I will thoroughly enjoy watching him create one of</span>
      <span class="ln">the world’s foremost golf performance companies.” <span class="by">-- Tod</span></span>
      <span class="ln by">Bramwell, 16 time NLK Circuit winner, Winner of the 2003</span>
      <span class="ln end by">Corvane Classic, 2010 Halvery Trophy Champion</span>
    </blockquote>

    <div class="polaroid" style="left:22px;top:666px;width:126px;height:146px;transform:rotate(-1deg)">
      <div class="shot" role="img" aria-label="Wendell Pruitt holding a trophy" style="background:linear-gradient(180deg,#7d96ad,#2a2e2c)"><span class="tag">WENDELL PRUITT</span></div>
    </div>
    <blockquote class="quote" style="left:168px;top:675px;width:205px">
      <span class="ln">“I trust and rely on Dale to get me</span>
      <span class="ln">ready for every round of golf that I</span>
      <span class="ln">play on the NLK Circuit. He is defi-</span>
      <span class="ln">nitely one of the best in the indus-</span>
      <span class="ln end">try.”</span>
    </blockquote>
    <p class="quote" style="left:20px;top:823px;width:353px">
      <span class="ln by">-- Wendell Pruitt, NLK Circuit Professional Golfer, Winner,</span>
      <span class="ln by">2007 Lyle Dunmore Vantrex Invitational, 2010 Ostrava Mutual</span>
      <span class="ln end by">Championship</span>
    </p>
  </section>

</div>
</body>
</html>
```